Bright Ledger Path LLC Seminar Workbook Template

Our mission: Our mission is to provide students with amazing accounting literacy experiences in amazing learning environments so they can accomplish amazing career and business goals.
We would like to have a Microsoft Word template that we can use for all of our course content. We are profession; yet not stuffy. We teach a timeless subject; yet we are very modern.
Our logo is attached. We would like our logo or parts of our logo to be incorporated into the template (for example, perhaps the tagline is included in the bottom right corner). We have also attached a sample of a company's work. We do not like their design; but it's the kind of end product that we are interested in.
We are grateful for anyone who is interested in this project. Thank you for your help.

```html
<!DOCTYPE html>
<html lang="en">
<head>
<meta charset="utf-8">
<title>Bright Ledger Path LLC – Workbook Page</title>
<link href="https://fonts.googleapis.com/css2?family=Roboto:wght@400;500;700&display=swap" rel="stylesheet">
<style>
  :root {
    --backdrop: #e6e6e6;
    --page: #ffffff;
    --green: #a8c21c;
    --blue: #1b9ccc;
    --ink: #444444;
  }
  * { margin: 0; padding: 0; box-sizing: border-box; }
  html, body { width: 1034px; height: 1200px; overflow: hidden; }
  body {
    background: var(--backdrop);
    font-family: "Roboto", Arial, sans-serif;
    color: var(--ink);
    position: relative;
  }
  .page {
    position: absolute;
    left: 139px; top: 65px;
    width: 756px; height: 1069px;
    background: var(--page);
  }
  .page-frame { position: absolute; left: 0; top: 0; }
  .brand-name {
    position: absolute;
    left: 0; right: 0; top: 90px;
    text-align: center;
    font-size: 40px;
    font-weight: 700;
    color: var(--blue);
    letter-spacing: 1px;
  }
  .column {
    position: absolute;
    top: 189px;
    width: 287px;
    height: 746px;
    overflow: hidden;
    font-size: 13px;
    line-height: 16.8px;
    text-align: justify;
  }
  .column p { margin-bottom: 16.8px; }
  .column p.run-on { margin-bottom: 0; }
  .column p.indent { text-indent: 9px; }
  .column-left { left: 77px; }
  .column-right { left: 387px; }
  .footer-note {
    position: absolute;
    left: 77px; top: 970px;
    font-size: 11px;
    color: var(--ink);
  }
  .footer-note .company { color: var(--green); font-size: 12px; margin-left: 3px; }
  .page-number {
    position: absolute;
    left: 365px; top: 999px;
    width: 24px; height: 24px;
    border-radius: 3px;
    background: var(--blue);
    color: #fff;
    font-size: 13px;
    font-weight: 700;
    line-height: 24px;
    text-align: center;
  }
</style>
</head>
<body>
  <div class="page">
    <svg class="page-frame" width="756" height="1069" viewBox="0 0 756 1069" aria-hidden="true">
      <rect x="51.5" y="56.5" width="651" height="956" rx="30" fill="none" stroke="var(--green)" stroke-width="3"/>
      <rect x="57.5" y="62" width="640" height="945" rx="25" fill="none" stroke="var(--blue)" stroke-width="1.5"/>
      <rect x="40" y="121" width="18" height="18" fill="var(--green)"/>
      <rect x="698" y="914" width="18" height="18" fill="var(--green)"/>
    </svg>

    <div class="brand-name">Bright Ledger Path</div>

    <div class="column column-left">
      <p class="indent">Lorem ipsum dolor sit amet, consectetur adipiscing elit. Etiam aliquam dolor tortor, et varius libero efficitur ac. Duis quis mi tincidunt orci sagittis mattis. Praesent scelerisque nec ipsum malesuada viverra. Phasellus tempus suscipit neque eu gravida. Integer vel commodo urna. Sed non diam id purus consectetur rhoncus. Suspendisse porttitor urna imperdiet viverra scelerisque. Nullam blandit, elit et faucibus lobortis, massa eros consectetur enim, condimentum placerat lacus nisl vitae eros. Integer dolor tellus, tristique vitae velit ut, posuere euismod lacus. Aliquam mattis libero ac venenatis consectetur. Maecenas congue tortor tellus, bibendum posuere ante rhoncus in. Praesent eros nisl, tristique nec neque ac, tempus mollis dolor. Nulla facilisi. Vivamus egestas enim felis, non vehicula diam hendrerit ac.</p>
      <p>Proin metus lectus, gravida eget dapibus in, pharetra nec sem. Vestibulum ut eros viverra, ultricies urna vitae, congue eros. Donec in dui et felis sollicitudin dictum a a eros. Vestibulum vulputate suscipit tempor. Cras lectus justo, aliquet eget lectus in, semper ultrices diam. Proin eget dignissim velit. Sed suscipit id tellus nec scelerisque.</p>
      <p>Donec eu nisl in mi venenatis tempus. Orci varius natoque penatibus et magnis dis parturient montes, nascetur ridiculus mus. Quisque feugiat, nisl quis egestas euismod, enim nulla congue tortor, congue vulputate justo dolor eu metus. Integer elementum vulputate fringilla. Nullam magna lectus, elementum eu bibendum in, mattis sit amet leo. Praesent accumsan eleifend gravida. Mauris volutpat turpis lobortis, aliquam sem ac, luctus libero. Nunc ullamcorper lorem quis suscipit rutrum. Nunc tempor et eros vel elementum. Ut cursus luctus ligula, sit amet posuere tortor rhoncus nec. Pellentesque vitae ipsum sem. Orci varius natoque penatibus et magnis dis parturient montes, nascetur ridiculus mus. In</p>
    </div>

    <div class="column column-right">
      <p class="run-on">libero nisi, facilisis eget convallis eget, euismod eget nunc. Suspendisse eu consectetur tortor, vel sodales lorem. Pellentesque a nibh porta nisi efficitur porttitor.</p>
      <p class="indent">Lorem ipsum dolor sit amet, consectetur adipiscing elit. Etiam aliquam dolor tortor, et varius libero efficitur ac. Duis quis mi tincidunt orci sagittis mattis. Praesent scelerisque nec ipsum malesuada viverra. Phasellus tempus suscipit neque eu gravida. Integer vel commodo urna. Sed non diam id purus consectetur rhoncus. Suspendisse porttitor urna imperdiet viverra scelerisque. Nullam blandit, elit et faucibus lobortis, massa eros consectetur enim, condimentum placerat lacus nisl vitae eros. Integer dolor tellus, tristique vitae velit ut, posuere euismod lacus. Aliquam mattis libero ac venenatis consectetur. Maecenas congue tortor tellus, bibendum posuere ante rhoncus in. Praesent eros nisl, tristique nec neque ac, tempus mollis dolor. Nulla facilisi. Vivamus egestas enim felis, non vehicula diam hendrerit ac.</p>
      <p>Proin metus lectus, gravida eget dapibus in, pharetra nec sem. Vestibulum ut eros viverra, ultricies urna vitae, congue eros. Donec in dui et felis sollicitudin dictum a a eros. Vestibulum vulputate suscipit tempor. Cras lectus justo, aliquet eget lectus in, semper ultrices diam. Proin eget dignissim velit. Sed suscipit id tellus nec scelerisque.</p>
      <p>Donec eu nisl in mi venenatis tempus. Orci varius natoque penatibus et magnis dis parturient montes, nascetur ridiculus mus. Quisque feugiat, nisl quis egestas euismod, enim nulla congue tortor, congue vulputate justo dolor eu metus. Integer elementum vulputate fringilla. Nullam magna lectus, elementum eu bibendum in, mattis sit amet leo. Praesent accumsan eleifend gravida. Mauris volutpat turpis lobortis, aliquam sem ac, luctus libero. Nunc ullamcorper lorem quis suscipit rutrum. Nunc tempor et eros vel elementum. Ut</p>
    </div>

    <div class="footer-note">(c) 2020 <span class="company">Bright Ledger Path LLC</span></div>
    <div class="page-number">1</div>
  </div>
</body>
</html>
```